Business Card Design Project - bel soravin group

dear Sirs

we need business card design for our group ( BEL Soravin Group ) , i have got the Logo design of our group from pixel harbor in previous , so all need details relating to our group i think available with you, as well as the the chosen logo design

we hope to provide us with business card logo that to be appropaite and satisfactory to us .

thanks

note : logo design of our group is attached .
Updates

Reason: please extend the deadline of my project for additional 15 days because i didn't received appropriate design for our gruop yet . kindly beaware that i have received 77 design till now , supossed to send me 200-250 design at least . thanks

Target Market(s)

contents
-

name : Korvan EL Mistrani

position : Operation Manager

Industry/Entity Type

Business

Requirements
Must have

• person name

group logo
Nice to have
• logo color matching with back background

```html
<!DOCTYPE html>
<html lang="en">
<head>
<meta charset="UTF-8">
<title>BEL Soravin Group – Business Card</title>
<link href="https://fonts.googleapis.com/css2?family=Lato:wght@400;700&display=swap" rel="stylesheet">
<style>
  :root {
    --page-bg: #e9e7e3;
    --card-white: #fbfbfb;
    --ink: #222428;
    --ink-soft: #3b3e44;
    --brand-blue: #1d4f9e;
    --blue-light: #1f6fd6;
    --blue-deep: #0a3a8f;
    --on-blue: #ffffff;
  }
  * { box-sizing: border-box; margin: 0; padding: 0; }
  html, body {
    width: 1200px; height: 720px; overflow: hidden;
    background: var(--page-bg);
    font-family: "Lato", sans-serif;
  }
  .sheet {
    position: relative; width: 1200px; height: 720px;
    display: flex; align-items: center; justify-content: center; gap: 40px;
  }
  .card {
    position: relative; width: 540px; height: 310px;
    box-shadow: 0 6px 18px rgba(0,0,0,0.18);
  }
  .card--front { background: var(--card-white); color: var(--ink); }
  .card--back {
    background: radial-gradient(ellipse at 50% 35%, var(--blue-light) 0%, var(--blue-deep) 85%);
    display: flex; align-items: center; justify-content: center;
  }
  .brand {
    display: flex; align-items: center; gap: 10px;
    font-weight: 700; letter-spacing: 0.04em; text-transform: uppercase;
    white-space: nowrap;
  }
  .brand__mark { display: block; background: currentColor; }
  .card--front .brand {
    position: absolute; top: 26px; right: 28px;
    color: var(--brand-blue); font-size: 21px;
  }
  .card--front .brand__mark { width: 14px; height: 14px; }
  .card--back .brand { color: var(--on-blue); font-size: 34px; gap: 14px; }
  .card--back .brand__mark { width: 22px; height: 22px; }

  .person { position: absolute; left: 30px; top: 138px; }
  .person__name { font-size: 24px; font-weight: 400; color: var(--ink); }
  .person__role { font-size: 14px; color: var(--ink-soft); margin-top: 3px; }

  .address {
    position: absolute; left: 318px; top: 92px;
    font-size: 13px; line-height: 1.35; color: var(--ink);
  }
  .phones {
    position: absolute; left: 318px; top: 160px;
    list-style: none; font-size: 14px; line-height: 1.45; color: var(--ink);
  }
  .phones li { display: flex; align-items: center; gap: 10px; }
  .phones svg { width: 13px; height: 13px; fill: var(--brand-blue); flex: none; }

  .online { position: absolute; left: 30px; bottom: 34px; font-size: 14px; line-height: 1.5; }
  .online__web { font-weight: 700; }
</style>
</head>
<body>
<main class="sheet">
  <section class="card card--front" aria-label="Card front">
    <div class="brand"><span class="brand__mark"></span>BEL Soravin Group</div>

    <div class="person">
      <h1 class="person__name">Korvan EL Mistrani</h1>
      <p class="person__role">Operation Manager</p>
    </div>

    <address class="address" style="font-style:normal">
      Avenue Marceline Dufort - Port Sable<br>
      BP 482 - Linoré, Valdesse
    </address>

    <ul class="phones">
      <li>
        <svg viewBox="0 0 16 16" aria-label="Telephone"><path d="M3 1h3l1.5 4-2 1.3a9 9 0 0 0 4.2 4.2L11 8.5l4 1.5v3a2 2 0 0 1-2 2A12 12 0 0 1 1 3a2 2 0 0 1 2-2z"/></svg>
        (318) 42 615 08 37
      </li>
      <li>
        <svg viewBox="0 0 16 16" aria-label="Fax"><path d="M4 1h7l2 2v3H4zM1 7h14v6h-3v2H4v-2H1zM5 11v3h6v-3z"/></svg>
        (318) 42 617 24 51
      </li>
      <li>
        <svg viewBox="0 0 16 16" aria-label="Mobile"><path d="M4 0h8a1 1 0 0 1 1 1v14a1 1 0 0 1-1 1H4a1 1 0 0 1-1-1V1a1 1 0 0 1 1-1zm1 2v10h6V2zm3 11a1 1 0 1 0 0 2 1 1 0 0 0 0-2z"/></svg>
        (318) 86 203 49 12
      </li>
    </ul>

    <div class="online">
      <p class="online__mail">korvan-mistrani@bel-soravin.com</p>
      <p class="online__web">www.bel-soravin.com</p>
    </div>
  </section>

  <section class="card card--back" aria-label="Card back">
    <div class="brand"><span class="brand__mark"></span>BEL Soravin Group</div>
  </section>
</main>
</body>
</html>
```